Looking for a clean, modern, and professional business card design that reflects Valtrim Systems

The design should include the company logo, contact details, and align with our brand identity. Please use a sophisticated and minimalist style, incorporating [specific colors, if applicable]. Creativity is welcome, but the card must maintain a polished and professional appearance.

Details to Include:

Name: Gavin Trelowe
Title: VP Sales / Operations
Company: Valtrim Systems
Phone: 483.216.7705
Email: gavin@valtrimsystems-example.com
Website: www.valtrimsystems-example.com

```html
<!DOCTYPE html>
<html lang="en">
<head>
<meta charset="utf-8">
<title>Valtrim Systems – Business Card</title>
<link rel="stylesheet" href="https://fonts.googleapis.com/css2?family=Poppins:wght@400;500;600;700&display=swap">
<style>
  :root {
    --page-bg: #4a4a4a;
    --front-dark: #050608;
    --front-mid: #151a20;
    --front-band: rgba(0, 0, 0, 0.35);
    --front-band-light: rgba(255, 255, 255, 0.03);
    --back-bg: #e9e8e9;
    --brand-blue: #3b74b6;
    --ink: #111111;
    --ink-soft: #2e2e2e;
    --divider: #c9c9cb;
    --white: #ffffff;
  }
  * { box-sizing: border-box; margin: 0; padding: 0; }
  html, body {
    width: 1200px; height: 1000px; overflow: hidden;
    background: var(--page-bg);
    font-family: "Poppins", sans-serif;
  }
  .canvas { position: relative; width: 1200px; height: 1000px; }

  .card {
    position: absolute; left: 188px; width: 824px; height: 470px;
    border-radius: 32px; overflow: hidden;
  }
  .card-front {
    top: 22px;
    background: radial-gradient(ellipse at 62% 50%, var(--front-mid) 0%, var(--front-dark) 75%);
  }
  .card-back { top: 508px; background: var(--back-bg); }

  .front-band {
    position: absolute; top: 0; bottom: 0;
  }
  .front-band-center { left: 237px; width: 352px; background: var(--front-band); }
  .front-band-right { left: 589px; right: 0; background: var(--front-band-light); }

  .wordmark {
    position: absolute; font-weight: 600; letter-spacing: 1px; white-space: nowrap;
  }
  .card-front .wordmark {
    left: 0; right: 0; top: 208px; text-align: center;
    font-size: 36px; color: var(--white);
  }
  .card-back .wordmark {
    left: 522px; top: 214px; font-size: 27px; color: var(--ink);
  }

  .contact-block {
    position: absolute; left: 22px; width: 420px; top: 88px; text-align: center;
  }
  .person-name { font-size: 30px; font-weight: 600; color: var(--brand-blue); line-height: 36px; }
  .person-title { font-size: 22px; font-weight: 500; color: var(--ink); line-height: 30px; margin-top: 4px; }
  .contact-list { list-style: none; margin-top: 31px; }
  .contact-list li {
    font-size: 19px; color: var(--ink-soft); line-height: 50px; white-space: nowrap;
  }

  .divider {
    position: absolute; left: 442px; top: 50px; width: 1px; height: 350px;
    background: var(--divider);
    box-shadow: 6px 0 18px rgba(0, 0, 0, 0.08);
  }
  .icon { position: absolute; left: 464px; width: 24px; height: 24px; }
  .icon-phone { top: 198px; }
  .icon-mail { top: 249px; }
  .icon-web { top: 299px; }
</style>
</head>
<body>
<div class="canvas">
  <section class="card card-front" aria-label="Card front">
    <div class="front-band front-band-center"></div>
    <div class="front-band front-band-right"></div>
    <div class="wordmark">Valtrim Systems</div>
  </section>

  <section class="card card-back" aria-label="Card back">
    <div class="contact-block">
      <h1 class="person-name">Gavin Trelowe</h1>
      <p class="person-title">VP Sales / Operations</p>
      <ul class="contact-list">
        <li>483.216.7705</li>
        <li>gavin@valtrimsystems-example.com</li>
        <li>www.valtrimsystems-example.com</li>
      </ul>
    </div>

    <div class="divider"></div>

    <svg class="icon icon-phone" viewBox="0 0 24 24" aria-hidden="true">
      <path fill="#3b74b6" d="M6.6 10.8c1.4 2.8 3.8 5.1 6.6 6.6l2.2-2.2c.3-.3.7-.4 1-.2 1.1.4 2.3.6 3.6.6.6 0 1 .4 1 1V20c0 .6-.4 1-1 1C10.6 21 3 13.4 3 4c0-.6.4-1 1-1h3.5c.6 0 1 .4 1 1 0 1.3.2 2.5.6 3.6.1.3 0 .7-.2 1z"/>
      <path fill="none" stroke="#3b74b6" stroke-width="1.6" stroke-linecap="round" d="M14 3.5a7 7 0 0 1 6.5 6.5M14 7a3.5 3.5 0 0 1 3 3"/>
    </svg>
    <svg class="icon icon-mail" viewBox="0 0 24 24" aria-hidden="true">
      <rect x="2" y="5" width="20" height="14" rx="1.5" fill="#3b74b6"/>
      <path d="M2.5 6l9.5 7 9.5-7" fill="none" stroke="#e9e8e9" stroke-width="1.4"/>
    </svg>
    <svg class="icon icon-web" viewBox="0 0 24 24" aria-hidden="true">
      <g fill="none" stroke="#3b74b6" stroke-width="1.8">
        <circle cx="12" cy="12" r="9"/>
        <ellipse cx="12" cy="12" rx="4" ry="9"/>
        <path d="M3 12h18M4.5 7.5h15M4.5 16.5h15"/>
      </g>
    </svg>

    <div class="wordmark">Valtrim Systems</div>
  </section>
</div>
</body>
</html>
```